I need a Canva design for my company for real estate new listings

A new listing Canva template for properties we list, also a sold and under contract template. We are an outdoor brand tallowbrookgroup.com so it needs to flow with our designs.

```html
<!DOCTYPE html>
<html lang="en">
<head>
<meta charset="utf-8">
<title>Under Contract – Red Oak Farm</title>
<link href="https://fonts.googleapis.com/css2?family=Poppins:wght@800;900&family=Playfair+Display:wght@400&family=Roboto:wght@400;500;700&display=swap" rel="stylesheet">
<style>
  :root {
    --paper: #efece6;
    --bark: #3d2a20;
    --clay: #8f5a35;
    --ink: #2e2420;
    --white: #ffffff;
  }
  * { box-sizing: border-box; margin: 0; padding: 0; }
  html, body { width: 1200px; height: 1200px; overflow: hidden; background: var(--paper); }
  .flyer { position: relative; width: 1200px; height: 1200px; background: var(--paper); font-family: 'Roboto', sans-serif; color: var(--ink); }
  .side-panel { position: absolute; left: 49px; top: 0; width: 434px; height: 1039px; background: var(--bark); }
  .brand { position: absolute; left: 49px; top: 160px; width: 434px; text-align: center; display: flex; align-items: center; justify-content: center; gap: 14px; }
  .brand-mark { width: 18px; height: 18px; background: var(--paper); }
  .brand-name { font-family: 'Roboto', sans-serif; font-weight: 500; font-size: 34px; color: var(--paper); letter-spacing: 1px; }
  .headline { position: absolute; left: 520px; top: 128px; font-family: 'Poppins', sans-serif; font-weight: 900; line-height: 0.86; letter-spacing: -1px; }
  .headline .line-dark { display: block; font-size: 106px; color: var(--bark); }
  .headline .line-accent { display: block; font-size: 106px; color: var(--clay); }
  .photo { position: absolute; border: 6px solid var(--white); }
  .photo-main { left: 62px; top: 339px; width: 600px; height: 450px; background: linear-gradient(180deg, #6f9fd8 0%, #8fb47a 35%, #6d8a45 60%, #b8ab88 100%); }
  .photo-garage { left: 64px; top: 808px; width: 292px; height: 205px; background: linear-gradient(180deg, #e7e4df 0%, #c8c4bd 55%, #8a8985 100%); }
  .photo-deck { left: 373px; top: 808px; width: 291px; height: 205px; background: linear-gradient(180deg, #2f5a22 0%, #4d7a3a 40%, #b3505a 62%, #c2606a 100%); }
  .description { position: absolute; left: 677px; top: 342px; width: 460px; font-size: 22px; line-height: 27.8px; text-align: justify; color: var(--ink); }
  .description p + p { margin-top: 27.8px; }
  .property-title { position: absolute; left: 685px; top: 778px; font-family: 'Playfair Display', serif; font-size: 44px; line-height: 48px; color: var(--clay); }
  .property-location { position: absolute; left: 687px; top: 872px; font-size: 31px; color: var(--clay); }
  .price { position: absolute; left: 687px; top: 928px; width: 241px; height: 74px; background: var(--clay); color: var(--white); font-weight: 700; font-size: 46px; display: flex; align-items: center; justify-content: center; }
  .accent-band { position: absolute; left: 0; top: 1039px; width: 1200px; height: 20px; background: var(--clay); }
  .footer { position: absolute; left: 0; top: 1059px; width: 1200px; height: 141px; background: var(--bark); }
  .contact-bar { position: absolute; left: 53px; top: 1083px; width: 1091px; height: 69px; border: 5px solid var(--white); display: flex; font-weight: 500; font-size: 27px; }
  .contact-bar > div { display: flex; align-items: center; justify-content: center; height: 100%; }
  .contact-label { width: 372px; background: var(--clay); color: var(--white); }
  .contact-phone { width: 289px; background: var(--white); color: var(--bark); gap: 10px; }
  .contact-web { flex: 1; background: var(--bark); color: var(--white); }
</style>
</head>
<body>
<div class="flyer">
  <div class="side-panel"></div>
  <div class="brand"><span class="brand-mark"></span><span class="brand-name">Tallowbrook Group</span></div>

  <h1 class="headline"><span class="line-dark">UNDER</span><span class="line-accent">CONTRACT</span></h1>

  <div class="photo photo-main" role="img" aria-label="Brick ranch house with trees, gravel drive and lawn"></div>
  <div class="photo photo-garage" role="img" aria-label="Interior of the attached two-car garage"></div>
  <div class="photo photo-deck" role="img" aria-label="Red wooden deck backing onto green trees"></div>

  <div class="description">
    <p>Opportunity awaits with this charming brick ranch located just outside the quaint town of Red Oak in Nashville, North Carolina. Situated on approximately one acre, this 1,828-square-foot home features three bedrooms and two bathrooms, offering a solid foundation for someone ready to make it their own.</p>
    <p>With its classic brick construction and functional layout, this property is an excellent candidate for renovation. Whether you're searching for a family home, an investment property, or a weekend project, this home offers the chance to add your personal style while building lasting value.</p>
  </div>

  <h2 class="property-title">Red Oak Farm<br>Brick Ranch House</h2>
  <div class="property-location">Nash County, NC</div>
  <div class="price">$99,000</div>

  <div class="accent-band"></div>
  <div class="footer"></div>
  <div class="contact-bar">
    <div class="contact-label">Get in touch:</div>
    <div class="contact-phone">
      <svg width="18" height="20" viewBox="0 0 24 24" aria-hidden="true"><path fill="#8f5a35" d="M6.6 10.8a15.1 15.1 0 0 0 6.6 6.6l2.2-2.2c.3-.3.7-.4 1-.2 1.1.4 2.3.6 3.6.6.6 0 1 .4 1 1V20c0 .6-.4 1-1 1A17 17 0 0 1 3 4c0-.6.4-1 1-1h3.5c.6 0 1 .4 1 1 0 1.3.2 2.5.6 3.6.1.3 0 .7-.2 1z"/></svg>
      (252) 555-0148
    </div>
    <div class="contact-web">www.tallowbrookgroup.com</div>
  </div>
</div>
</body>
</html>
```